Suche nur ein Redesignvorschlag (visuell), ohne Realisierung
Zielgruppe
Wir sind ein IT-Dienstleister im Bereich IT-Infrastruktur.
Aufgabenstellung
Modern und frisch. Unser Marketingkonzept: "your IT gardener" soll übernommen werden. Die Seite sollte mit Wordpress realisiert werden können.

```html
<!DOCTYPE html>
<html lang="de">
<head>
<meta charset="utf-8">
<title>beetnet – IT-Dienstleister</title>
<link href="https://fonts.googleapis.com/css2?family=Open+Sans:wght@300;400;600;700&display=swap" rel="stylesheet">
<style>
:root{
  --green:#1b7d2d;
  --green-dark:#156423;
  --ink:#333;
  --muted:#666;
  --logo:#6b6b6b;
  --topbar:#1f1f1f;
  --grey-band:#dadada;
  --white:#fff;
  --field:#bdbdbd;
}
*{box-sizing:border-box;margin:0;padding:0}
html,body{width:1200px;height:3743px;overflow:hidden}
body{font-family:'Open Sans',Arial,sans-serif;color:var(--ink);background:var(--white);position:relative}
.section{position:absolute;left:0;width:1200px}
.abs{position:absolute}
.section-title{position:absolute;left:0;width:1200px;text-align:center;color:var(--green);font-size:22px;font-weight:400;letter-spacing:.5px}
.section-sub{position:absolute;left:0;width:1200px;text-align:center;color:#555;font-size:10.5px;letter-spacing:.3px}
.badge-icon{position:absolute;left:585px;width:30px;height:30px;border-radius:50%;background:var(--green);border:3px solid #fff;display:flex;align-items:center;justify-content:center;z-index:2}

/* top bar */
.topbar{top:0;height:32px;background:var(--topbar);color:#ddd;font-size:9px}
.topbar .item{position:absolute;top:10px;display:flex;align-items:center;gap:6px}
.topbar .dot{width:8px;height:8px;border-radius:50%;background:var(--green)}
.social{position:absolute;top:0;left:822px;display:flex}
.social span{width:28px;height:32px;display:flex;align-items:center;justify-content:center}
.social span i{width:8px;height:8px;background:#bbb;display:block}
.social span.on{background:#000}

/* header */
.header{top:32px;height:74px;background:#fff}
.brand{position:absolute;left:244px;top:22px;display:flex;align-items:center;gap:8px}
.brand-mark{width:12px;height:12px;border-radius:50%;background:var(--green)}
.brand-name{font-size:28px;font-weight:400;color:var(--logo);letter-spacing:1px;line-height:30px}
.nav{position:absolute;left:455px;top:30px;display:flex;font-size:9.5px;color:#333}
.nav a{color:inherit;text-decoration:none;padding:0 12px;border-left:1px solid #999;line-height:10px}
.nav a:first-child{border:none;padding-left:0;color:var(--green);font-weight:600}
.nav-underline{position:absolute;left:446px;top:70px;width:40px;height:3px;background:var(--green)}

/* hero */
.hero{top:106px;height:355px;background:linear-gradient(180deg,#4a5a2a 0%,#7c8a3f 35%,#6d8b3a 60%,#556b2a 100%)}
.hero-photo{position:absolute;inset:0;background:radial-gradient(ellipse at 30% 40%,#8c6e7a 0%,rgba(140,110,122,0) 40%),radial-gradient(ellipse at 75% 55%,#9aa0a0 0%,rgba(154,160,160,0) 45%)}
.hero h1{position:absolute;left:487px;top:152px;color:#fff;font-weight:600;font-size:36px;line-height:42px;text-shadow:0 1px 3px rgba(0,0,0,.4)}
.hero p{position:absolute;left:487px;top:250px;width:440px;color:#fff;font-size:12.5px;font-weight:600;line-height:17px;text-shadow:0 1px 3px rgba(0,0,0,.5)}
.hero-arrow{position:absolute;top:166px;width:22px;height:22px;background:rgba(255,255,255,.35);display:flex;align-items:center;justify-content:center}

/* news */
.news{top:461px;height:492px;background:var(--grey-band)}
.btn-outline{position:absolute;left:875px;top:53px;width:81px;height:25px;border:1px solid #888;color:#666;font-size:8px;display:flex;align-items:center;justify-content:center}
.feature{position:absolute;left:244px;top:122px;width:356px;height:263px;background:linear-gradient(90deg,#2e3a22 0%,#44572a 45%,#6a7d3a 70%,#4e4a32 100%)}
.feature .shade{position:absolute;left:0;top:0;width:188px;height:100%;background:rgba(20,20,20,.55)}
.feature h3{position:absolute;left:18px;top:14px;color:#fff;font-size:14.5px;font-weight:400}
.feature p{position:absolute;left:18px;top:40px;width:164px;color:#eee;font-size:8.5px;line-height:14.2px}
.btn-green{position:absolute;background:var(--green);color:#fff;font-size:8.5px;display:flex;align-items:center;justify-content:center;font-weight:600}
.news-item{position:absolute;left:619px;width:340px;height:75px}
.date{position:absolute;left:0;top:0;width:62px;height:75px;background:#2b2b2b}
.date .day{height:58px;background:var(--green);color:#fff;font-size:27px;display:flex;align-items:center;justify-content:center}
.date .mon{height:17px;color:#fff;font-size:9px;display:flex;align-items:center;justify-content:center}
.news-item h4{position:absolute;left:75px;top:0;font-size:9.5px;font-weight:400;color:#222}
.news-item p{position:absolute;left:75px;top:16px;width:265px;font-size:7.2px;line-height:16.5px;color:#555}
.news-item p b{color:var(--green)}

/* portrait */
.portrait{top:953px;height:493px;background:#fff}
.portrait-text{position:absolute;left:244px;top:140px;width:356px;text-align:right;font-size:8.7px;line-height:14.5px;color:#444}
.portrait-text p{margin-bottom:14px}
.portrait-img{position:absolute;left:619px;top:124px;width:337px;height:261px;background:linear-gradient(180deg,#3f5b2a 0%,#5d7a3a 40%,#6f8a55 70%,#4b6330 100%)}

/* references */
.refs{top:1446px;height:568px;background:var(--grey-band)}
.ref-grid{position:absolute;left:131px;top:123px;width:938px;height:313px}
.tile{position:absolute}
.tile-client{position:absolute;left:234px;top:0;width:235px;height:313px;background:#2c3035;color:#fff;text-align:center}
.tile-client h5{margin-top:100px;font-size:14px;font-weight:400}
.tile-client p{margin:6px 20px 0;font-size:9px;line-height:14px;color:#ddd}

/* services */
.services{top:2014px;height:395px;background:#fff}
.service{position:absolute;top:140px;width:150px;text-align:center}
.service .ico{height:28px;display:flex;justify-content:center}
.service h4{font-size:12.5px;font-weight:400;margin-top:8px;color:#222;letter-spacing:.3px}
.service p{font-size:7.2px;line-height:10.5px;color:#777;margin-top:10px}

/* partners */
.partners{top:2409px;height:340px;background:var(--grey-band)}
.chip{position:absolute;height:26px;border-radius:3px;background:#b9b9b9}

/* contact */
.contact{top:2749px;height:443px;background:#fff}
.info-row{position:absolute;left:270px;display:flex;gap:10px;font-size:9.5px;color:#333;line-height:12px}
.field{position:absolute;height:24px;background:var(--field);border:1px solid #aaa;color:#eee;font-size:9.5px;padding:5px 8px}
.field.white{background:#fff;color:#999}

.map{top:3192px;height:218px;background:linear-gradient(135deg,#ebeae6 0%,#e2e1dc 50%,#ecebe7 100%)}
.remote{top:3410px;height:180px;background:var(--green);color:#fff}
.remote h3{position:absolute;left:0;width:1200px;top:36px;text-align:center;font-size:13.5px;font-weight:400}
.remote p{position:absolute;left:255px;top:72px;width:315px;text-align:right;font-size:10px;line-height:14.5px}
.remote .in{position:absolute;left:632px;width:170px;height:20px;background:var(--green);border:1px solid #fff;color:#fff;font-size:9.5px;padding:3px 6px}
.footer{top:3590px;height:153px;background:#fff}
.footer .brand{top:62px}
.footer .copy{position:absolute;left:417px;top:77px;font-size:8.5px;color:var(--green)}
.footer .links{position:absolute;left:718px;top:77px;display:flex;font-size:8.5px;color:#333}
.footer .links span{padding:0 12px;border-left:1px solid #999;line-height:9px}
.footer .links span:first-child{border:none;padding-left:0}
</style>
</head>
<body>

<div class="section topbar">
  <div class="item" style="left:246px"><span class="dot"></span>Hotline: 061 555 20 20</div>
  <div class="item" style="left:396px"><span class="dot"></span>Email: info@beetnet.ch</div>
  <div class="item" style="left:572px"><span class="dot"></span>Remote-Tool / Offline-Monitoring</div>
  <div class="social"><span><i></i></span><span><i></i></span><span class="on"><i></i></span><span><i></i></span><span><i></i></span></div>
</div>

<header class="section header">
  <div class="brand"><span class="brand-mark"></span><span class="brand-name">beetnet</span></div>
  <nav class="nav"><a>Home</a><a>Aktuelles</a><a>Portrait</a><a>Dienstleistungen</a><a>Partner</a><a>Kontakt</a></nav>
  <div class="nav-underline"></div>
</header>

<section class="section hero">
  <div class="hero-photo" role="img" aria-label="Foto: Schubkarre mit Pflanzen auf einer Wiese"></div>
  <div class="hero-arrow" style="left:30px"><svg width="10" height="10"><path d="M7 1 L3 5 L7 9" stroke="#fff" stroke-width="1.5" fill="none"/></svg></div>
  <div class="hero-arrow" style="left:1146px"><svg width="10" height="10"><path d="M3 1 L7 5 L3 9" stroke="#fff" stroke-width="1.5" fill="none"/></svg></div>
  <h1>IT-gardening<br>– Beet für Beet zum Erfolg!</h1>
  <p>Informatik ist wie ein Garten – damit er gedeiht und Freude bereitet, muss er gehegt, gepflegt und regelmässig unterhalten werden.</p>
</section>

<section class="section news">
  <div class="badge-icon" style="top:-15px"><svg width="14" height="12"><rect x="1" y="1" width="12" height="9" fill="none" stroke="#fff" stroke-width="1.3"/><line x1="3" y1="4" x2="11" y2="4" stroke="#fff"/><line x1="3" y1="7" x2="8" y2="7" stroke="#fff"/></svg></div>
  <h2 class="section-title" style="top:42px">AKTUELLES</h2>
  <div class="section-sub" style="top:68px">NEUIGKEITEN AUS DER IT-WELT</div>
  <div class="btn-outline">ALLE NEWS</div>

  <article class="feature">
    <div role="img" aria-label="Foto: junge Pflanzensprösslinge in Erde" style="position:absolute;inset:0"></div>
    <div class="shade"></div>
    <h3>IT-Check / TCO Study</h3>
    <p>Ein gut durchdachtes IT-System ist gerade zu Krisenzeiten zu einem erheblichen Wettbewerbsfaktor geworden. Unternehmen sind mehr denn je gefordert, im IT-Bereich stets „up to date“ zu sein und die TCO Kosten laufend zu reduzieren. Während in grossen Unternehmen die TCO eine grosse Rolle für das IT-Management bedeutet, müssen KMU's darauf achten, dass Sie Konkurrenzfähig sind.</p>
    <div class="btn-green" style="left:18px;top:208px;width:83px;height:24px">Weiterlesen</div>
  </article>

  <div class="news-item" style="top:122px"><div class="date"><div class="day">02</div><div class="mon">AUG</div></div><h4>TITEL DER NEWS</h4><p>Lorem ipsum dolor sit amet, consectetuer adipiscing elit. Aenean commodo ligula eget dolor. Aenean massa. Cum sociis natoque penatibus et magnis dis parturient montes, nascetur ridiculus mus <b>...weiterlesen</b></p></div>
  <div class="news-item" style="top:216px"><div class="date"><div class="day">02</div><div class="mon">AUG</div></div><h4>TITEL DER NEWS</h4><p>Lorem ipsum dolor sit amet, consectetuer adipiscing elit. Aenean commodo ligula eget dolor. Aenean massa. Cum sociis natoque penatibus et magnis dis parturient montes, nascetur ridiculus mus <b>...weiterlesen</b></p></div>
  <div class="news-item" style="top:310px"><div class="date"><div class="day">02</div><div class="mon">AUG</div></div><h4>TITEL DER NEWS</h4><p>Lorem ipsum dolor sit amet, consectetuer adipiscing elit. Aenean commodo ligula eget dolor. Aenean massa. Cum sociis natoque penatibus et magnis dis parturient montes, nascetur ridiculus mus <b>...weiterlesen</b></p></div>
</section>

<section class="section portrait">
  <div class="badge-icon" style="top:-15px"><svg width="12" height="12"><circle cx="6" cy="3.5" r="2.6" fill="#fff"/><path d="M1 12 Q6 4 11 12Z" fill="#fff"/></svg></div>
  <h2 class="section-title" style="top:42px">PORTRAIT</h2>
  <div class="section-sub" style="top:68px">ZUVERLÄSSIG UND MOTIVIERT</div>
  <div class="portrait-text">
    <p>Als renommiertes Informatik-Unternehmen im Herzen des Kantons Aargau haben wir uns zum Ziel gesetzt, unseren unverwechselbaren Fingerabdruck in Ihrem Unternehmen zu hinterlassen.</p>
    <p>Als Ihr IT-Partner stellen wir uns ganz auf Ihre Bedürfnisse ein und entwickeln mit Ihnen zusammen die für Sie massgeschneiderte IT-Infrastruktur- und Datenhaltungs-Lösung.</p>
    <p>Unser täglicher Antrieb und Motivation in der Partnerschaft zu unseren Kunden sehen wir in dem Aufbau, der ENTWICKLUNG UND PFLEGE EINER IT-KULTUR, im Bereich Informatik-Infrastruktur und Datenhaltung.</p>
    <p>IT ist wie ein Garten: Für den wachsenden Erfolg eines Unternehmens braucht es eine fundierte Analyse, sorgfältige Planung und Implementierung sowie kontinuierliche Pflege und Bereicherung des IT-Oeko-Systems.</p>
  </div>
  <div class="portrait-img" role="img" aria-label="Foto: terrassierte Gartenbecken mit Seerosen"></div>
</section>

<section class="section refs">
  <div class="badge-icon" style="top:-15px"><svg width="14" height="10"><ellipse cx="7" cy="5" rx="6" ry="4" fill="#fff"/></svg></div>
  <h2 class="section-title" style="top:42px">REFERENZEN</h2>
  <div class="section-sub" style="top:68px">KUNDEN SIND KOMPLIMENTE</div>
  <div class="ref-grid">
    <div class="tile" role="img" aria-label="Screenshot einer Kunden-Website mit Familienfoto" style="left:0;top:0;width:234px;height:156px;background:linear-gradient(180deg,#eef2f5 0%,#c9b9a8 60%,#a89482 100%)"></div>
    <div class="tile" role="img" aria-label="Screenshot einer Kunden-Website eines Bauunternehmens" style="left:0;top:156px;width:234px;height:157px;background:linear-gradient(180deg,#d11e3c 0%,#d11e3c 15%,#8a6a55 40%,#5d5a55 100%)"></div>
    <div class="tile-client"><h5>KUNDENTITEL</h5><p>Lorem ipsum dolor sit amet, consectetuer adipiscing elit. Aenean commodo ligula eget dolor. Aenean massa. Cum sociis natoque penatibus et magnis dis parturient montes, nascetur ridiculus mus. Donec quam felis, ultricies nec, pellentesque eu, pretium quis, sem.</p></div>
    <div class="tile" role="img" aria-label="Screenshot einer Spital-Website mit Gebäudeansicht" style="left:469px;top:0;width:235px;height:156px;background:linear-gradient(180deg,#ffffff 0%,#ffffff 30%,#cfd5db 55%,#6f8aa6 100%)"></div>
    <div class="tile" role="img" aria-label="Screenshot einer Kunden-Website mit Produktbild" style="left:469px;top:156px;width:235px;height:157px;background:linear-gradient(180deg,#ffffff 0%,#ffffff 45%,#d6dde6 70%,#aebdcc 100%)"></div>
    <div class="tile" role="img" aria-label="Screenshot einer Versicherungs-Website" style="left:704px;top:0;width:234px;height:156px;background:linear-gradient(180deg,#f1f4f7 0%,#dfe7ee 70%,#7aa0c8 100%)"></div>
    <div class="tile" role="img" aria-label="Screenshot einer Website eines Elektro- und Gebäudetechnikbetriebs" style="left:704px;top:156px;width:234px;height:157px;background:linear-gradient(180deg,#ffffff 0%,#ffffff 40%,#e3edf4 60%,#e8eef3 100%)"></div>
  </div>
  <div class="btn-green" style="left:561px;top:454px;width:80px;height:24px">MEHR</div>
</section>

<section class="section services">
  <div class="badge-icon" style="top:-15px"><svg width="14" height="14"><circle cx="7" cy="7" r="4" fill="none" stroke="#fff" stroke-width="2.5" stroke-dasharray="2 1.2"/><circle cx="7" cy="7" r="1.6" fill="#fff"/></svg></div>
  <h2 class="section-title" style="top:42px">DIENSTLEISTUNGEN</h2>
  <div class="section-sub" style="top:68px">HANDEL UND DIENSTLEISTUNG IM EINKLANG</div>

  <div class="service" style="left:245px"><div class="ico"><svg width="24" height="22"><circle cx="9" cy="6" r="4" fill="#1b7d2d"/><path d="M2 20 Q9 8 16 20Z" fill="#1b7d2d"/><rect x="15" y="10" width="7" height="5" fill="#1b7d2d"/></svg></div><h4>CONSULTING</h4><p>Neue Projekte bedürfen einer sorgfältigen Planung und Organisation zur Lösung. Ressourcen und finanzielle Mittel müssen im Einklang stehen. Ihr IT-Consultant hilft Ihnen durch die IST-SOLL Aufnahme, durch Analysen, Workshops und Audits bei der Beratung, Planung und Umsetzung Ihrer neuen IT-Landschaft.</p></div>
  <div class="service" style="left:431px"><div class="ico"><svg width="24" height="22"><rect x="2" y="13" width="6" height="6" fill="none" stroke="#1b7d2d" stroke-width="1.5"/><rect x="15" y="3" width="6" height="6" fill="none" stroke="#1b7d2d" stroke-width="1.5"/><path d="M8 16 H12 V6 H15" stroke="#1b7d2d" stroke-width="1.5" fill="none"/></svg></div><h4>PROJEKTUMSETZUNG</h4><p>Einsatz von System Engineer Spezialisten mit einer ganzheitlichen Betrachtungsweise für das jeweilige Fachthema. Jedes Projekt beinhaltet eine Abnahme und Dokumentation des umgesetzten Auftrages.</p></div>
  <div class="service" style="left:619px"><div class="ico"><svg width="24" height="22"><circle cx="12" cy="11" r="7" fill="none" stroke="#1b7d2d" stroke-width="2"/><circle cx="12" cy="11" r="2.5" fill="#1b7d2d"/></svg></div><h4>HANDEL</h4><p>Durch den direkten und engen Kontakt zu führenden IT-Herstellern und Distributoren erlaubt es uns, Ihnen als Kunde eine faire und interessante Preisgestaltung in der Handelsbeschaffung (Hardware, Software, Lizenzmanagement) anzubieten.</p></div>
  <div class="service" style="left:805px"><div class="ico"><svg width="24" height="22"><circle cx="12" cy="11" r="7" fill="none" stroke="#1b7d2d" stroke-width="2"/><circle cx="12" cy="11" r="2.5" fill="#1b7d2d"/></svg></div><h4>SERVICES + SUPPORT</h4><p>Die Abrundung und Sicherstellung der gewünschten Leistungserfüllung erfolgt mit unseren qualitativ hochwertigen und kompetenten Dienstleistungen, die wie folgt aussehen:<br><br>• Hard- und Software-Support<br>• Störfallbehebung<br>• Online- und offline Monitoring<br>• Präventivwartung<br>• Ressourcenmanagement</p></div>
</section>

<section class="section partners">
  <div class="badge-icon" style="top:-15px"><svg width="14" height="10"><ellipse cx="7" cy="5" rx="6" ry="4" fill="#fff"/></svg></div>
  <h2 class="section-title" style="top:42px">PARTNER</h2>
  <div class="section-sub" style="top:68px">DIE BEETNET AG IST ZERTIFIZIERTER PARTNER VON</div>
  <div class="chip" role="img" aria-label="Partnerabzeichen" style="left:324px;top:125px;width:76px"></div>
  <div class="chip" role="img" aria-label="Partnerabzeichen" style="left:450px;top:116px;width:74px;height:44px"></div>
  <div class="chip" role="img" aria-label="Partnerabzeichen" style="left:575px;top:121px;width:74px;height:30px;background:#9fb0c8"></div>
  <div class="chip" role="img" aria-label="Partnerabzeichen" style="left:700px;top:116px;width:56px;height:44px"></div>
  <div class="chip" role="img" aria-label="Partnerabzeichen" style="left:797px;top:131px;width:80px;height:16px"></div>
  <div class="chip" role="img" aria-label="Partnerabzeichen" style="left:386px;top:202px;width:92px;height:48px"></div>
  <div class="chip" role="img" aria-label="Partnerabzeichen" style="left:496px;top:210px;width:88px;height:28px"></div>
  <div class="chip" role="img" aria-label="Partnerabzeichen" style="left:594px;top:206px;width:100px;height:34px;background:#d9a08e"></div>
  <div class="chip" role="img" aria-label="Partnerabzeichen" style="left:727px;top:208px;width:86px;height:30px"></div>
</section>

<section class="section contact">
  <div class="badge-icon" style="top:-15px"><svg width="12" height="14"><path d="M6 13 C1 7 1 5 1 5 A5 5 0 0 1 11 5 C11 5 11 7 6 13Z" fill="#fff"/><circle cx="6" cy="5" r="1.8" fill="#1b7d2d"/></svg></div>
  <h2 class="section-title" style="top:42px">KONTAKT</h2>
  <div class="section-sub" style="top:68px">STANDORT UND ANFAHRTSPLAN</div>

  <div class="info-row" style="top:128px"><svg width="10" height="12"><path d="M5 11 C1 6 1 4.5 1 4.5 A4 4 0 0 1 9 4.5 C9 4.5 9 6 5 11Z" fill="#1b7d2d"/></svg><div>Beetnet AG<br>Gartenweg 12<br>5000 Musterberg / Aargau</div></div>
  <div class="info-row" style="top:181px"><svg width="10" height="10"><path d="M1 2 Q1 9 8 9 L9 7 L7 6 L6 7 Q3 6 3 4 L4 3 L3 1Z" fill="#1b7d2d"/></svg><div>061 555 20 20</div></div>
  <div class="info-row" style="top:207px"><svg width="10" height="10"><rect x="1" y="3" width="8" height="5" fill="#1b7d2d"/><rect x="3" y="1" width="4" height="3" fill="#1b7d2d"/></svg><div>061 555 20 23</div></div>
  <div class="info-row" style="top:233px"><svg width="10" height="10"><rect x="1" y="2" width="8" height="6" fill="#1b7d2d"/><path d="M1 2 L5 5 L9 2" stroke="#fff" fill="none"/></svg><div>info@beetnet.ch</div></div>

  <div class="field white" style="left:484px;top:125px;width:228px">Name</div>
  <div class="field" style="left:731px;top:125px;width:228px">Firma</div>
  <div class="field" style="left:484px;top:169px;width:228px">Email</div>
  <div class="field" style="left:731px;top:169px;width:228px">Funktion</div>
  <div class="field" style="left:484px;top:212px;width:228px">Telefon</div>
  <div class="field" style="left:731px;top:212px;width:228px">Fax</div>
  <div class="field" style="left:484px;top:256px;width:475px;height:94px">Ihr Anliegen</div>
  <div class="btn-green" style="left:484px;top:369px;width:81px;height:23px">SENDEN</div>
</section>

<div class="section map" role="img" aria-label="Strassenkarte mit Standortmarkierung der Firma"></div>

<section class="section remote">
  <h3>REMOTE-TOOL / OFFLINE-MONITORING</h3>
  <p>Um Supportanfragen schneller und einfacher zu klären, gewähren Sie unseren Mitarbeitern via Remote-Support einen Blick auf Ihren Bildschirm. Das Programm muss nicht installiert werden, sondern Sie starten es direkt per Knopfdruck aus dem Internet.</p>
  <div class="in" style="top:76px">Name</div>
  <div class="in" style="top:106px">Support-Schlüssel</div>
  <div class="abs" style="left:814px;top:106px;width:66px;height:20px;background:#fff;color:var(--green);font-size:9px;font-weight:600;display:flex;align-items:center;justify-content:center">SENDEN</div>
</section>

<footer class="section footer">
  <div class="badge-icon" style="top:-15px"><svg width="12" height="12"><path d="M6 1 L11 6 H8 V11 H4 V6 H1Z" fill="#fff"/></svg></div>
  <div class="brand"><span class="brand-mark"></span><span class="brand-name">beetnet</span></div>
  <div class="copy">©2016 Beetnet AG. All rights reserved.</div>
  <div class="links"><span>HOME</span><span>KONTAKT</span><span>IMPRESSUM</span></div>
</footer>

</body>
</html>
```